I need Business Cards and Letterhead Designed

I have a current label so I just need the template design. It should be clean and should look rich. I own a Wealth Management/Investment Advisory business and I need to brand to look substantial & mature.

The Business Cards may be one or two sided and may be a standard or non-standard size. I will likely print on very thick stock but not a requirement. Embossment or foil are also something that I may consider but is not required.
Updates

Getting some great designs, thank you all for your hard work. I have returned from a trip and will be posting individual feedback over the next day or so. In the meantime please note the following:

1st. My disclosure should be posted at the bottom or back of the card. It may be in smaller print but it must be listed as follows "all together";

Securities offered through Pelgrave Brokerage, Inc. A Registered Broker/Dealer. Member NOBKA/DEXO. Gil Prawley, Registered Representative. Advisory Services offered through Halden Brightwell an RBO Registered Investment Advisory Firm. RJV Wealth Management, Pelgrave Brokerage and Halden Brightwell are unaffiliated. CA Insurance Lic.# 0K42573

2nd. My Title should be listed as President / CEO
&
I need the following contact information included:

Address:
418 Verlow Blvd
Suite 740
Costa Mesa, CA  92626

Phone; 949-555-0173
fax: 800-555-0148
email: gil.prawley@pelgravebrokerage.com

Thank you for your help.

Best regards,

GP

Target Market(s)

Affluent Individuals & Families. C-Level Executives, Women, Accountants, Attorneys, Business Owners

Industry/Entity Type

Business

Requirements
Must have
• Both my cards and letterhead must include the following disclosure:

Securities offered through Pelgrave Brokerage, Inc. A Registered Broker/Dealer. Member NOBKA/DEXO.
Gil Prawley, Registered Representative. Advisory Services offered through Halden Brightwell an RBO Registered Investment Advisory Firm. RJV Wealth Management, Pelgrave Brokerage and Halden Brightwell are unaffiliated. CA Insurance Lic.# 0K4257
Should not have
• Do not include illustrations of money bags or gold bullion, or "$" signs or anything of that type.

```html
<!DOCTYPE html>
<html lang="en">
<head>
<meta charset="utf-8">
<title>RJV Wealth Management – Letterhead</title>
<link href="https://fonts.googleapis.com/css2?family=Jost:wght@400;500&display=swap" rel="stylesheet">
<style>
  :root {
    --backdrop: #e9e4dc;
    --paper: #ffffff;
    --brand-brown: #7a3118;
    --brand-brown-light: #9a4a2a;
    --brand-brown-dark: #5e2410;
    --ink: #3a2a22;
    --ink-soft: #8a8580;
    --watermark: #e6e1dc;
  }
  * { box-sizing: border-box; margin: 0; padding: 0; }
  html, body { width: 1200px; height: 720px; overflow: hidden; }
  body {
    background: var(--backdrop);
    font-family: "Jost", "Futura", sans-serif;
    color: var(--ink);
    position: relative;
  }
  .sheet {
    position: absolute;
    top: 40px;
    width: 495px;
    height: 640px;
    box-shadow: 0 2px 10px rgba(0,0,0,0.12);
  }
  .letterhead { left: 75px; background: var(--paper); }
  .letterhead-back { left: 630px; background: var(--brand-brown); overflow: hidden; }

  .brand {
    position: absolute;
    top: 34px; left: 34px;
    display: flex; align-items: center; gap: 8px;
  }
  .brand-square {
    width: 14px; height: 14px;
    background: var(--brand-brown);
  }
  .brand-name {
    font-size: 17px; font-weight: 500;
    color: var(--brand-brown);
    letter-spacing: 0.04em;
  }
  .brand-tagline {
    position: absolute;
    top: 58px; left: 56px;
    font-size: 6.5px; color: var(--ink-soft);
    letter-spacing: 0.06em;
  }

  .contact {
    position: absolute;
    top: 28px; right: 28px;
    list-style: none;
    font-size: 6.5px;
    line-height: 9.5px;
    color: var(--ink-soft);
  }
  .contact li { display: flex; align-items: flex-start; gap: 5px; }
  .contact svg { width: 7px; height: 7px; flex: none; margin-top: 1px; fill: var(--ink-soft); }

  .watermark {
    position: absolute;
    top: 270px; left: 0; right: 0;
    text-align: center;
    font-size: 64px; font-weight: 500;
    letter-spacing: 0.3em;
    color: var(--watermark);
  }

  .disclosure {
    position: absolute;
    bottom: 18px; left: 40px; right: 40px;
    text-align: center;
    font-size: 5.4px; line-height: 7.5px;
    color: var(--ink);
  }

  .back-pattern {
    position: absolute; inset: 0;
    background: radial-gradient(ellipse at 50% 45%, var(--brand-brown-light) 0%, var(--brand-brown) 45%, var(--brand-brown-dark) 100%);
  }
  .back-name {
    position: absolute;
    top: 300px; left: 0; right: 0;
    text-align: center;
    font-size: 26px; font-weight: 500;
    letter-spacing: 0.3em;
    color: var(--paper);
  }
</style>
</head>
<body>
  <section class="sheet letterhead">
    <div class="brand">
      <span class="brand-square"></span>
      <span class="brand-name">RJV Wealth Management</span>
    </div>
    <p class="brand-tagline">Planning, Investment &amp; Retirement</p>

    <ul class="contact">
      <li><svg viewBox="0 0 10 10"><path d="M5 0a3.5 3.5 0 0 0-3.5 3.5C1.5 6 5 10 5 10s3.5-4 3.5-6.5A3.5 3.5 0 0 0 5 0zm0 5a1.5 1.5 0 1 1 0-3 1.5 1.5 0 0 1 0 3z"/></svg><span>418 Verlow Blvd Suite 740<br>Costa Mesa, CA 92626</span></li>
      <li><svg viewBox="0 0 10 10"><path d="M2 0l2 2.5-1 1.2c.6 1.3 1.6 2.3 2.9 2.9L7 5.6 9.5 7.5 8.5 10C4 10 0 6 0 1.5z"/></svg><span>949-555-0173</span></li>
      <li><svg viewBox="0 0 10 10"><rect x="2" y="0" width="6" height="3"/><rect x="0" y="3.5" width="10" height="5"/><rect x="2" y="7" width="6" height="3"/></svg><span>800-555-0148</span></li>
      <li><svg viewBox="0 0 10 10"><path d="M0 2h10v6H0z M0 2l5 3.5L10 2" fill="none" stroke="#8a8580" stroke-width="1"/></svg><span>gil.prawley@pelgravebrokerage.com</span></li>
    </ul>

    <div class="watermark">RJV</div>

    <p class="disclosure">Securities offered through Pelgrave Brokerage, Inc. A Registered Broker/Dealer. Member NOBKA/DEXO. Gil Prawley, Registered Representative. Advisory Services offered through Halden Brightwell<br>an RBO Registered Investment Advisory Firm. RJV Wealth Management, Pelgrave Brokerage and Halden Brightwell are unaffiliated. CA Insurance Lic.# 0K42573</p>
  </section>

  <section class="sheet letterhead-back">
    <div class="back-pattern" role="img" aria-label="Subtle tone-on-tone zigzag pattern across a deep brown ground"></div>
    <div class="back-name">RJV</div>
  </section>
</body>
</html>
```